Law Firm Needs a new Website Design

We need a new website design for our law firm located in Manhattan (Law Offices of Branford T. Quellsworth, PLLC).
We have an existing logo that we will to continue using, which can be found in www.QuellsworthLaw.example.
The Peak Counsel, Prime Advocates Logo should also be reflected near the bottom of the Home page.
The website will be 6 pages.

Deliverables:
I want a
1) home page,
2) About Us/Practice Areas page,
3) attorneys,
4) News and Articles page, and
5) Contact and Directions/Privacy Policy page.

The colors of my logo should be in the website.
I also like a touch of black and red.

The website should project "excellence."
We seek to provide the highest quality legal services.
We handle estate planning, wills, trusts, planning for people with disabilities, asset protection and preservation, Medicaid planning, hospital safe discharge, nursing home placement, powers of attorney, health care proxies, living wills, guardianships, probate, estate administration and related litigation.

I would like the colors of my Logo used (including shading where appropriate).
I also want some black on the borders and/or bottom and some red touches throughout the page.

My Logo should appear everywhere that "Law Offices Of Branford T. Quellsworth, PLLC" appears.
I want the badges for Peak counsel, Prime Advocates, Prime Legal Houses, and ZELK on the Home page.
I do not want too much text on the home page.

We would also like the website to have coding.
The final design should also communicate quality, expertise and stability.
Great start so far by the people who submitted designs.
Thank you.

Industry/Entity Type

Law Firm

Coding

Coded - Design and coding required

Number of Pages Required

5+ page

Colors
3276b5
ec1f27
474747

Requirements
Must have
• Please use my logo each time you mention Law Offices of Branford T. Quellsworth, PLLC. Please include the Peakcounsel, Prime Advocates, Prime Legal Houses and Zelk rating Badges on the web home page. I only wish to be contacted by phone. I am not including testimonials and am only using the New York City address.
Nice to have
• Prefer illustrations to photos regarding practice areas
Should not have
• Testimonials, contact me by email, free consultation.

```html
<!DOCTYPE html>
<html lang="en">
<head>
<meta charset="utf-8">
<title>Law Offices of Branford T. Quellsworth, PLLC</title>
<link href="https://fonts.googleapis.com/css2?family=Lato:ital,wght@0,400;0,700;1,400&family=Open+Sans:ital,wght@0,400;0,600;1,400&display=swap" rel="stylesheet">
<style>
  :root {
    --navy: #2a3363;
    --navy-deep: #222a55;
    --blue: #3276b5;
    --red: #ec1f27;
    --red-dark: #c4161c;
    --ink: #474747;
    --black: #050505;
    --white: #ffffff;
    --rule: #dcdfe6;
  }
  * { box-sizing: border-box; margin: 0; padding: 0; }
  html, body { width: 1200px; height: 1000px; overflow: hidden; }
  body { position: relative; background: var(--black); font-family: "Open Sans", sans-serif; color: var(--ink); }

  .site-header { position: absolute; top: 0; left: 0; width: 1200px; height: 86px; background: var(--white); }
  .brand { position: absolute; left: 202px; top: 10px; display: flex; align-items: center; gap: 14px; }
  .brand-mark { width: 58px; height: 58px; background: var(--blue); }
  .brand-name { font-family: "Lato", sans-serif; font-weight: 400; font-size: 19px; line-height: 1.25; color: var(--navy); width: 300px; }
  .header-phone { position: absolute; right: 180px; top: 30px; font-family: "Lato", sans-serif; font-size: 24px; color: var(--blue); }

  .main-nav { position: absolute; top: 86px; left: 0; width: 1200px; height: 32px; background: var(--navy); border-top: 1px solid #3b4680; }
  .main-nav ul { list-style: none; display: flex; position: absolute; left: 190px; top: 0; height: 31px; }
  .main-nav li { font-family: "Lato", sans-serif; font-size: 11.5px; color: var(--white); padding: 0 11.5px; line-height: 31px; border-right: 1px solid #3d4884; letter-spacing: .2px; }
  .main-nav li.is-active { background: #b0151b; padding: 0 17px; }

  .hero-backdrop { position: absolute; top: 118px; left: 0; width: 1200px; height: 882px;
    background: radial-gradient(ellipse at 50% 10%, #4a4a4e 0%, #2a2a2c 35%, #111 70%, #050505 100%); }
  .hero-title { position: absolute; top: 165px; left: 0; width: 1200px; text-align: center; font-family: "Lato", sans-serif; font-size: 29px; line-height: 34px; color: var(--white); }
  .hero-title .accent { color: var(--red); font-weight: 700; }
  .hero-title .underlined { font-weight: 700; text-decoration: underline; text-decoration-thickness: 2px; text-underline-offset: 4px; }

  .content-panel { position: absolute; top: 316px; left: 189px; width: 846px; height: 618px; background: var(--white); border-top: 3px solid var(--red); }
  .panel-band { height: 63px; background: var(--navy); display: flex; align-items: center; }
  .panel-band h2 { font-family: "Lato", sans-serif; font-weight: 400; color: var(--white); font-size: 26px; }
  .band-profile { position: absolute; left: 35px; top: 24px; }
  .band-areas { position: absolute; left: 575px; top: 27px; font-size: 22px !important; }

  .profile { position: absolute; left: 41px; top: 100px; width: 480px; font-size: 10.6px; line-height: 15px; }
  .profile p { margin-bottom: 15px; }
  .profile .name { color: var(--red); }
  .profile a { color: #1f5a9a; font-style: italic; text-decoration: underline; }
  .attorney { display: flex; align-items: center; gap: 14px; margin-top: 4px; }
  .attorney-photo { width: 82px; height: 101px; background: linear-gradient(160deg, #6d86a8, #3e4f68); }
  .attorney-name { font-style: italic; color: #111; font-size: 10.6px; }

  .practice-list { position: absolute; left: 577px; top: 100px; width: 225px; list-style: none; }
  .practice-list li { display: flex; gap: 12px; padding: 7px 0 7px 5px; border-bottom: 1px solid var(--rule); font-size: 9.6px; line-height: 15px; color: var(--ink); letter-spacing: .3px; text-transform: uppercase; }
  .practice-list svg { flex: none; margin-top: 1px; }
  .call-box { position: absolute; left: 577px; top: 369px; width: 225px; height: 72px; background: var(--red-dark); color: var(--white); text-align: center; font-family: "Lato", sans-serif; font-weight: 700; }
  .call-label { margin-top: 10px; font-size: 14px; letter-spacing: 1.5px; display: flex; align-items: center; justify-content: center; gap: 12px; }
  .call-label::before, .call-label::after { content: ""; width: 40px; height: 1px; background: rgba(255,255,255,.7); }
  .call-number { font-size: 23px; margin-top: 2px; }

  .panel-footer { position: absolute; left: 0; top: 470px; width: 846px; height: 148px; background: linear-gradient(to bottom, #ffffff 0%, #2a3363 30%, #2a3363 100%); color: var(--white); }
  .contact-col { position: absolute; top: 72px; font-size: 12px; line-height: 15px; }
  .col-address { left: 41px; }
  .col-phone { left: 278px; }
  .divider { position: absolute; top: 62px; width: 1px; height: 56px; background: rgba(255,255,255,.35); }
  .ratings { position: absolute; left: 520px; top: 52px; width: 148px; text-align: center; font-family: "Lato", sans-serif; color: #c9cde0; }
  .ratings .peak { font-size: 20px; padding-bottom: 8px; border-bottom: 1px solid rgba(255,255,255,.35); }
  .ratings .prime { font-size: 19px; margin-top: 8px; display: flex; align-items: center; justify-content: center; gap: 8px; }
  .ratings .prime::before { content: ""; width: 14px; height: 14px; background: #3276b5; }
  .badge { position: absolute; left: 730px; top: 50px; width: 56px; height: 72px; background: linear-gradient(#d4d6dc, #8e929c); border-radius: 3px; }

  .site-footer { position: absolute; top: 964px; left: 189px; width: 846px; font-size: 9.5px; color: #ddd; display: flex; justify-content: space-between; }
</style>
</head>
<body>
  <header class="site-header">
    <div class="brand">
      <span class="brand-mark"></span>
      <span class="brand-name">Law Offices of Branford T. Quellsworth, PLLC</span>
    </div>
    <div class="header-phone">(212) 555-0147</div>
  </header>

  <nav class="main-nav">
    <ul>
      <li class="is-active">HOME</li>
      <li>ABOUT US</li>
      <li>PRACTICE AREAS</li>
      <li>ATTORNEYS</li>
      <li>NEWS AND ARTICLES</li>
      <li>CONTACT AND DIRECTIONS</li>
      <li>PRIVACY POLICY</li>
    </ul>
  </nav>

  <div class="hero-backdrop" role="img" aria-label="Night skyline of Manhattan seen from above in dark grey tones"></div>
  <h1 class="hero-title">We <span class="accent">care about our clients</span> and<br><i>believe in</i> <span class="underlined">cultivating long-term<br>relationships</span>.</h1>

  <main class="content-panel">
    <div class="panel-band">
      <h2 class="band-profile">Firm Profile</h2>
      <h2 class="band-areas">Practice Areas</h2>
    </div>

    <section class="profile">
      <p>Our firm was founded in 1993 by <span class="name">Branford T. Quellsworth</span>, a member of the National Guild of Senior Care Counsel (NGSCC) and an elder law practitioner for over 19 years. Our firm is uniquely positioned to provide quality legal advice and representation in regards to <a>estate planning</a>, <a>wills</a>, <a>trusts</a>, <a>planning for people with disabilities</a>, <a>asset protection and preservation</a>, <a>Medicaid planning</a>, <a>hospital safe discharge</a>, <a>nursing home placement</a>, <a>powers of attorney</a>, <a>health care proxies</a>, <a>living wills</a>, <a>guardianships</a>, <a>probate</a>, <a>estate administration and related litigation</a>.</p>
      <p>Our familiarity with entitlement programs such as Medicaid and the statutes and regulations pertaining to them, our sensitivity to the problems and needs of seniors and our access to geriatric care managers enable us to help families preserve their life savings while planning for the care of a spouse, a parent or loved one who has dementia, Alzheimer's or other long-term health care needs.</p>
      <p>We care about our clients and believe in cultivating long-term relationships. We strive to maintain the dignity, independence and well-being of our clients and respond to them quickly with the consideration and respect they deserve.</p>
      <div class="attorney">
        <div class="attorney-photo" role="img" aria-label="Portrait photo of the founding attorney"></div>
        <span class="attorney-name">Branford T. Quellsworth</span>
      </div>
    </section>

    <ul class="practice-list">
      <li><svg width="13" height="12" viewBox="0 0 13 12"><path d="M1 6.5l3.5 4L12 1" fill="none" stroke="#3276b5" stroke-width="2.6"/></svg>Estate Planning</li>
      <li><svg width="13" height="12" viewBox="0 0 13 12"><path d="M1 6.5l3.5 4L12 1" fill="none" stroke="#3276b5" stroke-width="2.6"/></svg>Probate and Estate Administration</li>
      <li><svg width="13" height="12" viewBox="0 0 13 12"><path d="M1 6.5l3.5 4L12 1" fill="none" stroke="#3276b5" stroke-width="2.6"/></svg>Powers of Attorney, Health Care Proxies and Other Advanced Directives</li>
      <li><svg width="13" height="12" viewBox="0 0 13 12"><path d="M1 6.5l3.5 4L12 1" fill="none" stroke="#3276b5" stroke-width="2.6"/></svg>Supplemental Needs Trusts</li>
      <li><svg width="13" height="12" viewBox="0 0 13 12"><path d="M1 6.5l3.5 4L12 1" fill="none" stroke="#3276b5" stroke-width="2.6"/></svg>Medicaid Planning and Assistance with the Application Process</li>
      <li><svg width="13" height="12" viewBox="0 0 13 12"><path d="M1 6.5l3.5 4L12 1" fill="none" stroke="#3276b5" stroke-width="2.6"/></svg>Guardianships</li>
      <li><svg width="13" height="12" viewBox="0 0 13 12"><path d="M1 6.5l3.5 4L12 1" fill="none" stroke="#3276b5" stroke-width="2.6"/></svg>Residential Real Estate</li>
    </ul>

    <div class="call-box">
      <div class="call-label">CALL US</div>
      <div class="call-number">(212) 555-0147</div>
    </div>

    <div class="panel-footer">
      <div class="contact-col col-address">318 Harlow Avenue, Suite 1204<br>New York, New York 10120</div>
      <span class="divider" style="left:236px"></span>
      <div class="contact-col col-phone">Telephone: (212) 555-0147<br>Fax: (212) 555-0198</div>
      <span class="divider" style="left:475px"></span>
      <div class="ratings">
        <div class="peak">Peak Counsel</div>
        <div class="prime">Prime Advocates</div>
      </div>
      <div class="badge" role="img" aria-label="Firm ranking badge"></div>
    </div>
  </main>

  <footer class="site-footer">
    <span>Home | About Us | Contact Us</span>
    <span>Copyrights© 2016 Law Offices of Branford T. Quellsworth, PLLC</span>
  </footer>
</body>
</html>
```